Electronic Repair Company need a new flyer!

Hi Guys,

I need a new flyer for my repair company that I can use for my door 2 door marketing. The flyers will be send to thousands of addresses in the Netherlands. You can design the flyer in English but I need to be able to translate the flyer into Dutch, so I might need the PSD file.

We repair Computers, Laptops and ALL Quorvel devices.

For some inspiration please take a look at: www.fixmeerkat.nl

And see the pictures below ;)

Target Market(s)

Computer & Smartphone Repair

Industry/Entity Type

Electronic

Requirements
Nice to have
• I would like to have some pictures from our staff (like on our website) in it so people can see who we really are :)

```html
<!DOCTYPE html>
<html lang="en">
<head>
<meta charset="utf-8">
<title>FixMeerkat.nl repair flyer</title>
<link rel="stylesheet" href="https://fonts.googleapis.com/css2?family=Montserrat:wght@800;900&family=Roboto:wght@400;500;700;900&family=Roboto+Condensed:wght@700&family=Arimo:wght@400&display=swap">
<style>
:root{
  --stage:#9a9a9a;
  --red:#e5432c;
  --dark:#2e2e2e;
  --night:#141418;
  --white:#ffffff;
  --ink:#222222;
  --ring:#c9c9c9;
}
*{margin:0;padding:0;box-sizing:border-box}
html,body{width:1200px;height:1200px;overflow:hidden;background:var(--stage)}
.flyer{position:absolute;left:213px;top:52px;width:829px;height:1172px;transform:scale(.9375);transform-origin:0 0;background:var(--white);overflow:hidden;font-family:"Roboto",sans-serif}
.abs{position:absolute}
.hero-bg{left:0;top:0;width:829px;height:640px;background:radial-gradient(ellipse at 70% 35%,#3a3a44 0%,#1d1d23 45%,var(--night) 100%)}
.staff-photo{left:20px;top:120px;width:360px;height:500px;border-radius:45% 45% 6px 6px;background:linear-gradient(180deg,#c98a6a 0%,#e9e6e2 35%,#f07a2a 45%,#eeeeee 60%,#d9d9d9 100%);opacity:.9}
.swoosh{left:0;top:0;width:829px;height:1172px}
.brand{left:25px;top:30px;display:flex;align-items:center;gap:10px;font-family:"Roboto",sans-serif;font-weight:900;font-size:40px;color:var(--white)}
.brand-square{width:34px;height:34px;background:var(--red)}
.headline{right:17px;top:82px;text-align:right;color:var(--white)}
.headline .quickly{font-family:"Montserrat",sans-serif;font-weight:900;font-size:84px;line-height:88px;color:var(--red);letter-spacing:2px}
.headline .quality{font-family:"Roboto Condensed",sans-serif;font-weight:700;font-size:62px;line-height:62px}
.headline .nowin{font-family:"Roboto Condensed",sans-serif;font-weight:700;font-size:36px;line-height:44px}
.tagline{right:17px;top:277px;text-align:right;font-family:"Roboto Condensed",sans-serif;font-weight:700;font-size:28px;line-height:28px;color:var(--red)}
.badge{left:398px;top:475px;width:186px;height:186px;border-radius:50%;background:var(--ring);padding:8px;box-shadow:0 4px 10px rgba(0,0,0,.35)}
.badge-inner{width:100%;height:100%;border-radius:50%;background:var(--dark);border:5px solid var(--red);color:var(--white);text-align:center;padding-top:44px}
.badge-small{font-size:26px;line-height:28px}
.badge-big{font-family:"Roboto Condensed",sans-serif;font-weight:700;font-size:62px;line-height:60px}
.service-title{left:402px;top:677px;width:427px;height:52px;background:var(--red);color:#f4f4f4;font-family:"Roboto Condensed",sans-serif;font-weight:700;font-size:42px;line-height:52px;text-align:center}
.service-panel{left:416px;top:729px;width:413px;height:289px;background:var(--dark)}
.service-list{list-style:none;padding:20px 0 0 22px}
.service-item{display:flex;align-items:center;height:54.5px;color:var(--white);font-size:24px;font-weight:500}
.service-icon{width:36px;height:36px;background:var(--red);margin-right:16px;display:flex;align-items:center;justify-content:center}
.service-icon span{width:18px;height:18px;border:2px solid var(--white);border-radius:2px}
.tab{left:0;height:42px;background:var(--red);color:var(--white);border-radius:0 21px 21px 0;padding-left:13px;box-shadow:0 8px 8px -4px rgba(0,0,0,.25)}
.tab-about{top:661px;width:304px;font-weight:700;font-size:19px;line-height:42px;letter-spacing:1.3px}
.tab-call{top:988px;width:260px;font-size:19px;line-height:42px}
.about{left:14px;top:727px;width:312px;font-family:"Arimo",sans-serif;font-size:18.5px;line-height:20.5px;color:var(--ink)}
.about p+p{margin-top:21px}
.phone{left:14px;top:1060px;display:flex;align-items:center;gap:8px;font-family:"Roboto",sans-serif;font-weight:700;font-size:49px;color:var(--ink)}
.web{left:15px;top:1131px;display:flex;align-items:center;gap:12px;color:var(--white);font-size:25px;height:42px}
.partners{left:390px;top:1068px;width:430px;display:grid;grid-template-columns:repeat(4,1fr);row-gap:22px;color:var(--white);font-weight:900;font-size:19px;text-align:center}
</style>
</head>
<body>
<main class="flyer">
  <div class="abs hero-bg" role="img" aria-label="Dark close-up photo of a laptop keyboard"></div>
  <div class="abs staff-photo" role="img" aria-label="Photo of a smiling technician in an orange and white polo holding an open laptop and a charger cable"></div>

  <svg class="abs swoosh" viewBox="0 0 829 1172" aria-hidden="true">
    <path d="M0 515 C120 610 300 610 440 590 L829 560 L829 1172 L0 1172 Z" fill="#ffffff"/>
    <path d="M0 470 C60 560 240 600 400 590 C300 640 120 650 0 580 Z" fill="var(--red)"/>
    <path d="M416 640 C560 540 720 510 829 580 L829 1030 L416 1030 Z" fill="var(--dark)"/>
    <path d="M560 530 C660 470 760 480 829 500 L829 610 C760 520 660 520 560 530 Z" fill="var(--red)"/>
    <path d="M580 540 C680 510 770 520 829 560 L829 575 C770 535 680 525 580 540 Z" fill="#ffffff"/>
    <path d="M402 677 L416 677 L416 736 Z" fill="#a82a1a"/>
    <path d="M395 1035 L829 1035 L829 1172 L0 1172 L0 1130 L350 1130 Z" fill="var(--red)"/>
    <path d="M0 1122 L355 1122 L350 1130 L0 1130 Z" fill="#e6e6e6"/>
  </svg>

  <div class="abs brand"><span class="brand-square"></span>FIXMEERKAT.NL</div>

  <div class="abs headline">
    <div class="quickly">QUICKLY</div>
    <div class="quality">QUALITATIVELY</div>
    <div class="nowin">AND ON A NO WIN NO FEE!</div>
  </div>
  <div class="abs tagline">We repair your social and<br>business life!</div>

  <div class="abs badge"><div class="badge-inner">
    <div class="badge-small">repair with</div>
    <div class="badge-big">24 hr!</div>
  </div></div>

  <div class="abs service-title">Our Service</div>
  <section class="abs service-panel">
    <ul class="service-list">
      <li class="service-item"><span class="service-icon"><span></span></span>QUORVEL REPAIR</li>
      <li class="service-item"><span class="service-icon"><span></span></span>COMPUTER REPAIR</li>
      <li class="service-item"><span class="service-icon"><span></span></span>LAPTOP REPAIR</li>
      <li class="service-item"><span class="service-icon"><span></span></span>TABLET REPAIR</li>
      <li class="service-item"><span class="service-icon"><span></span></span>SMARTPHONE REPAIR</li>
    </ul>
  </section>

  <div class="abs tab tab-about">Pleasant, we FixMeerkat.nl</div>
  <div class="abs about">
    <p>More than 20 technicians are six days a week, ready to repair your device as soon as possible. Because we have more than 1.2 million parts center in stock, we can often fix within 24 hours of your device!</p>
    <p>With us you can go for the repair of your Quorvel Desk or Quorvel Book. Quorvel help our specialists will be happy with a professional</p>
  </div>
  <div class="abs tab tab-call">Call our customer service</div>

  <div class="abs phone">
    <svg width="30" height="30" viewBox="0 0 30 30" aria-hidden="true"><rect width="30" height="30" rx="6" fill="var(--ink)"/><path d="M9 7c1-1 2-1 3 0l2 3c.5 1 0 2-1 2.5 1 2 2.5 3.5 4.5 4.5.5-1 1.5-1.5 2.5-1l3 2c1 1 1 2 0 3-2 2-5 1-8-1.5S8 13 7.5 11 8 8 9 7z" fill="#fff"/></svg>
    088-0123456
  </div>
  <div class="abs web">
    <svg width="24" height="24" viewBox="0 0 24 24" aria-hidden="true"><g fill="none" stroke="#fff" stroke-width="2.5"><rect x="2" y="8" width="11" height="7" rx="3.5" transform="rotate(45 7.5 11.5)"/><rect x="11" y="9" width="11" height="7" rx="3.5" transform="rotate(45 16.5 12.5)"/></g></svg>
    www.fixmeerkat.nl
  </div>

  <div class="abs partners">
    <span>SOLVANE</span><span>HEXPO</span><span>LUNARO</span><span>FENSTREL</span>
    <span>TAVRIX</span><span>ARAVO</span><span>SEMORA</span><span>DELVO</span>
  </div>
</main>
</body>
</html>
```